Silver Creek Plumbing Business card & letter head design

We need a new business card and letter head for our plumbing company called silver creek plumbing. attached is the companys logo. We provide domestic and commercial plumbing services in regional western Australia. We are after Something simple yet nice to look at and something that fits within the trade industry.

Target Market(s)

trade/building industry

Contact Information for Business Card

Darl Hensby
Manager
0461 238 574
enquiries@scplumbwork.net.au
ABN: 47 381 905 462
PCL: 5187

Domestic & Commercial Plumbing
Tip Truck & Excavator hire

Colors

Designer to choose colors to be used in the design.

```html
<!DOCTYPE html>
<html lang="en">
<head>
<meta charset="utf-8">
<title>Silver Creek Plumbing — Stationery</title>
<link rel="stylesheet" href="https://fonts.googleapis.com/css2?family=Open+Sans:wght@400;600;700&display=swap">
<style>
  :root {
    --brand-blue: #1f5fb0;
    --ink: #3d3d3d;
    --ink-soft: #6b6b6b;
    --rule: #b9bcc2;
    --paper: #fbfbfb;
    --backdrop: #e4e5e7;
  }
  * { box-sizing: border-box; margin: 0; padding: 0; }
  html, body { width: 979px; height: 1200px; overflow: hidden; }
  body {
    background: var(--backdrop);
    font-family: "Open Sans", Arial, sans-serif;
    color: var(--ink);
    position: relative;
  }
  .sheet {
    position: absolute; background: var(--paper);
    box-shadow: 0 6px 18px rgba(0,0,0,.12);
  }
  .wordmark {
    font-family: "Open Sans", Arial, sans-serif;
    font-weight: 700; color: var(--brand-blue);
    text-transform: uppercase; line-height: 1.05; letter-spacing: .02em;
    display: flex; align-items: center; gap: 8px;
  }
  .wordmark .mark-square { background: var(--brand-blue); flex: none; }

  /* Letterhead */
  .letterhead { left: 220px; top: 28px; width: 540px; height: 764px; }
  .letterhead .wordmark { position: absolute; left: 44px; top: 44px; font-size: 17px; }
  .letterhead .mark-square { width: 14px; height: 14px; }
  .letter-body { position: absolute; left: 58px; top: 150px; width: 424px; font-size: 10.5px; line-height: 1.5; }
  .salutation { font-weight: 700; font-size: 12px; margin-bottom: 12px; }
  .letter-body p { margin-bottom: 14px; text-align: justify; }
  .signature { width: 130px; height: 44px; margin-top: 6px; background: linear-gradient(90deg,#e9e9eb,#f3f3f4); }
  .letter-footer { position: absolute; left: 0; right: 0; bottom: 28px; height: 90px; }
  .footer-rule { position: absolute; left: 44px; right: 110px; top: 34px; border-top: 1px solid var(--rule); }
  .web-tab {
    position: absolute; right: 34px; top: 25px; height: 18px; padding: 0 16px;
    background: var(--brand-blue); color: #fff; font-size: 9.5px; line-height: 18px;
    clip-path: polygon(8px 0,100% 0,calc(100% - 8px) 100%,0 100%);
  }
  .footer-details { position: absolute; left: 44px; top: 44px; padding-left: 12px; border-left: 5px solid var(--brand-blue); font-size: 9px; line-height: 1.45; }
  .footer-details b { color: var(--brand-blue); }
  .footer-details .services { color: var(--ink-soft); font-size: 10px; margin-top: 2px; }

  /* Business cards */
  .card { top: 868px; width: 340px; height: 194px; }
  .card-contact { left: 130px; }
  .card-brand { left: 510px; }
  .card-contact .wordmark { position: absolute; left: 22px; top: 26px; font-size: 13px; }
  .card .mark-square { width: 11px; height: 11px; }
  .card-holder { position: absolute; right: 24px; top: 22px; text-align: right; }
  .card-holder .name { color: var(--brand-blue); font-weight: 700; font-size: 10px; text-transform: uppercase; }
  .card-holder .role { font-size: 8.5px; color: var(--ink-soft); }
  .card-rule { position: absolute; left: 22px; right: 90px; top: 92px; border-top: 1px solid var(--rule); }
  .card-contact .web-tab { right: 14px; top: 84px; height: 15px; line-height: 15px; font-size: 8px; padding: 0 12px; }
  .card-details { position: absolute; left: 22px; top: 118px; padding-left: 10px; border-left: 4px solid var(--brand-blue); font-size: 8.5px; line-height: 1.55; }
  .card-details .row { display: flex; align-items: center; gap: 5px; }
  .card-details svg { width: 8px; height: 8px; fill: var(--ink); }
  .card-details b { color: var(--brand-blue); }
  .card-brand .wordmark { position: absolute; left: 0; right: 0; top: 70px; justify-content: center; font-size: 17px; }
  .card-brand .mark-square { width: 14px; height: 14px; }
  .card-web { position: absolute; left: 0; right: 0; top: 138px; display: flex; justify-content: center; align-items: center; gap: 8px; font-size: 8.5px; color: var(--brand-blue); }
  .card-web::before, .card-web::after { content: ""; width: 26px; border-top: 1px solid var(--brand-blue); }
</style>
</head>
<body>
  <section class="sheet letterhead">
    <div class="wordmark"><span class="mark-square"></span><span>Silver Creek<br>Plumbing</span></div>
    <div class="letter-body">
      <p class="salutation">Dear Mr. Hale,</p>
      <p>Lorem Ipsum is simply dummy text of the printing and typesetting industry. Lorem Ipsum has been the industry's standard dummy text ever since the 1500s, when an unknown printer took a galley of type and scrambled it to make a type specimen book. It has survived not only five centuries, but also the leap into electronic typesetting, remaining essentially unchanged.</p>
      <p>The standard chunk of Lorem Ipsum used since the 1500s is reproduced below for those interested. Sections 1.10.32 and 1.10.33 from "de Finibus Bonorum et Malorum" by Tullus are also reproduced in their exact original form, accompanied by English versions from the 1914 translation by H. Morland.</p>
      <p>Lorem Ipsum is simply dummy text of the printing and typesetting industry. Lorem Ipsum has been the industry's standard dummy text ever since the 1500s, when an unknown printer took a galley of type and scrambled it to make a type specimen book. It has survived not only five centuries, but also the leap into electronic typesetting, remaining essentially unchanged. It was popularised in the</p>
      <p>Lorem Ipsum is simply dummy text of the printing and typesetting industry. Lorem Ipsum has been the industry's standard dummy text ever since the 1500s, when an unknown printer took a galley of type and scrambled it to make a type specimen book. It has survived not only five centuries, but also the leap into electronic typesetting, remaining essentially unchanged. It was popularised in the</p>
      <div class="signature" role="img" aria-label="Handwritten signature"></div>
    </div>
    <footer class="letter-footer">
      <div class="footer-rule"></div>
      <div class="web-tab">www.scplumbwork.net.au</div>
      <div class="footer-details">
        <div><b>ABN:</b> 47 381 905 462 &nbsp;|&nbsp; <b>PCL:</b> 5187</div>
        <div><b>Tel:</b> 0461 238 574 &nbsp;<b>Mail:</b> enquiries@scplumbwork.net.au</div>
        <div class="services">Domestic &amp; Commercial Plumbing &nbsp;|&nbsp; Tip Truck &amp; Excavator hire</div>
      </div>
    </footer>
  </section>

  <section class="sheet card card-contact">
    <div class="wordmark"><span class="mark-square"></span><span>Silver Creek<br>Plumbing</span></div>
    <div class="card-holder"><div class="name">Darl Hensby</div><div class="role">Manager</div></div>
    <div class="card-rule"></div>
    <div class="web-tab">www.scplumbwork.net.au</div>
    <div class="card-details">
      <div class="row"><svg viewBox="0 0 10 10"><path d="M2 0.5l2 2-1 1.3c.6 1.3 1.4 2.1 2.7 2.7L7 5.5l2 2-1.2 1.8C4.5 9 1 5.5.7 1.7z"/></svg>0461 238 574</div>
      <div class="row"><svg viewBox="0 0 10 10"><path d="M0 2h10v6H0zM0 2l5 3.5L10 2v1L5 6.5 0 3z" fill-rule="evenodd"/></svg>enquiries@scplumbwork.net.au</div>
      <div><b>ABN:</b> 47 381 905 462 &nbsp;|&nbsp; <b>PCL:</b> 5187</div>
    </div>
  </section>

  <section class="sheet card card-brand">
    <div class="wordmark"><span class="mark-square"></span><span>Silver Creek<br>Plumbing</span></div>
    <div class="card-web">www.scplumbwork.net.au</div>
  </section>
</body>
</html>
```